Online Certificate in Research Methods needs a Digital Banner ad

We are launching an online graduate certificate in Quantitative and Qualitative Social Science Research Methods. We need a digital banner created so we can advertise on plimora, zentrik, and some other places.

The banner needs to use these color schemes and fonts: https://universityrelations.marlowecrest.edu/brand-guide/color

Would like the banner to say (either as three lines, or if not in three lines, have these sets of words at minimum on the same line):
Online Graduate Certificate in
Quantitative & Qualitative
Social Science Research Methods

We also want it to say Marlowe Crest University and Next Start Date August 18, 2021. I’ve attached a picture of a version we tried to create but is hard to read.

We need a graphic that looks good in the following specs:
600px wide x 70px tall, high quality (at least 300 dpi) jpg or png

And
Plimora recommendations:
Design Recommendations
• File Type: JPG or PNG
• Ratio: 1.91:1 to 1:1
• Resolution: At least 1080 x 1080 pixels
Text Recommendations
• Primary Text: 125 characters
• Headline: 40 characters
• Description: 30 characters
Technical Requirements
• Maximum File Size: 30MB
• Minimum Width: 600 pixels
• Minimum Height: 600 pixels
• Aspect Ratio Tolerance: 3%

```html
<!DOCTYPE html>
<html lang="en">
<head>
<meta charset="utf-8">
<title>Marlowe Crest University – Online Graduate Certificate</title>
<link rel="stylesheet" href="https://fonts.googleapis.com/css2?family=Libre+Baskerville&family=Montserrat:wght@600;700&family=Outfit:wght@700&family=Questrial&display=swap">
<style>
  :root {
    --navy: #002855;
    --gold: #eaaa00;
    --white: #ffffff;
    --photo-warm: #8a5a3a;
    --photo-light: #c8b4a0;
    --photo-green: #2f8a78;
  }
  html, body {
    margin: 0;
    padding: 0;
    overflow: hidden;
    background: var(--navy);
  }
  .banner {
    position: relative;
    width: 1200px;
    height: 628px;
    background: var(--navy);
    overflow: hidden;
    font-family: "Montserrat", sans-serif;
  }
  .banner__art {
    position: absolute;
    inset: 0;
  }
  .brand {
    position: absolute;
    left: 44px;
    top: 40px;
    display: flex;
    align-items: center;
    gap: 14px;
  }
  .brand__mark {
    width: 34px;
    height: 34px;
    background: var(--gold);
  }
  .brand__name {
    font-family: "Libre Baskerville", serif;
    font-size: 33px;
    color: var(--white);
    letter-spacing: -0.5px;
    line-height: 1;
  }
  .accent-bar {
    position: absolute;
    left: 14px;
    top: 123px;
    width: 11px;
    height: 402px;
    background: var(--gold);
  }
  .headline {
    position: absolute;
    left: 46px;
    top: 158px;
    margin: 0;
    font-family: "Outfit", sans-serif;
    font-weight: 700;
    font-size: 47px;
    color: var(--white);
    white-space: nowrap;
    line-height: 1;
  }
  .program {
    position: absolute;
    left: 40px;
    top: 275px;
    width: 610px;
    margin: 0;
    font-family: "Questrial", sans-serif;
    font-weight: 400;
    font-size: 47px;
    line-height: 54px;
    color: var(--white);
    text-align: center;
  }
  .start-date {
    position: absolute;
    left: 18px;
    top: 540px;
    margin: 0;
    font-weight: 700;
    font-size: 30px;
    color: var(--navy);
    letter-spacing: -0.4px;
    white-space: nowrap;
    line-height: 1;
  }
  .cta {
    position: absolute;
    left: 618px;
    top: 546px;
    width: 178px;
    text-align: center;
    font-weight: 700;
    font-size: 23px;
    color: var(--navy);
    letter-spacing: 0.3px;
    text-decoration: none;
    white-space: nowrap;
    line-height: 1;
  }
</style>
</head>
<body>
  <div class="banner">
    <svg class="banner__art" width="1200" height="628" viewBox="0 0 1200 628">
      <defs>
        <linearGradient id="photoTones" x1="0" y1="0" x2="1" y2="1">
          <stop offset="0" stop-color="var(--photo-light)"/>
          <stop offset="0.35" stop-color="var(--photo-warm)"/>
          <stop offset="1" stop-color="var(--photo-green)"/>
        </linearGradient>
      </defs>
      <polygon class="band band--date" points="0,525 487,525 564,594 0,594" fill="var(--white)"/>
      <polygon class="band band--cta" points="528,525 853,525 892,594 604,594" fill="var(--white)"/>
      <polygon class="chevron" points="901,0 948,0 735,305 960,628 915,628 688,305" fill="var(--gold)"/>
      <polygon class="photo" role="img" aria-label="Photo of a smiling student with headphones and a backpack, holding a red folder" points="948,0 1200,0 1200,628 960,628 735,305" fill="url(#photoTones)"/>
    </svg>

    <div class="brand">
      <span class="brand__mark"></span>
      <span class="brand__name">Marlowe Crest University</span>
    </div>

    <div class="accent-bar"></div>

    <h1 class="headline">Online Graduate Certificate</h1>
    <p class="program">Quantitative &amp; Qualitative<br>Social Science Research<br>Methods</p>

    <p class="start-date">Next Start Date August 18, 2021</p>
    <a class="cta" href="#">LEARN MORE</a>
  </div>
</body>
</html>
```